Redesign of page from emergency manual

Please redesign this PDF to look better. Please don't include any stock photos. It must be legible. Making some words bold is probably a good idea.

Here are some things I like :

https://tarrowbooks.com.au/collections/frontpage/products/the-plk-v2-ebook

https://img-cd.vostramediafiles.com/qa-ejkwPLOTYY_SuCKbZNu411Qwgjv8YssPxEdzXN93hDkSRjLXK8WmfgbmrJW4ZZ3yUPK=w1052-h592-rw

```html
<!DOCTYPE html>
<html lang="en">
<head>
<meta charset="utf-8">
<title>Hypertension, Acute</title>
<link href="https://fonts.googleapis.com/css2?family=Poppins:wght@400;500;600;700;800&display=swap" rel="stylesheet">
<style>
:root{
  --navy:#0b2540;
  --slate:#3d4a58;
  --blue:#2d62f0;
  --blue-deep:#2347e8;
  --teal:#2e9e9c;
  --grey-panel:#ebe9ea;
  --ink:#1b2430;
  --red:#d9141b;
  --white:#ffffff;
  --page-bg:#d4d4d4;
}
*{margin:0;padding:0;box-sizing:border-box}
html,body{width:1200px;height:960px;overflow:hidden;background:var(--page-bg)}
body{font-family:'Poppins',sans-serif;color:var(--ink)}
.card{position:absolute;left:0;top:16px;width:1505px;height:1163px;background:var(--white);transform:scale(0.7973);transform-origin:0 0;overflow:hidden}
.abs{position:absolute}
.header-art{left:0;top:0}
.title{left:58px;top:42px;font-size:62px;font-weight:700;color:var(--white);letter-spacing:.5px}
.subtitle{left:830px;top:52px;font-size:23px;font-weight:700;line-height:27px;color:var(--white)}
.page-tab{left:1362px;top:0;width:123px;height:186px;background:var(--blue);border-radius:0 0 14px 14px;color:var(--white);font-size:112px;font-weight:800;text-align:center;line-height:186px;letter-spacing:-6px;padding-right:6px}
.side-bar{left:1385px;top:186px;width:76px;height:977px;background:var(--slate)}
.side-title{left:1423px;top:250px;writing-mode:vertical-rl;font-size:40px;font-weight:800;color:var(--white);transform:translateX(-50%);letter-spacing:.5px}
.revision{left:1403px;top:820px;width:40px;height:280px;background:var(--blue);border-radius:20px;color:var(--white);writing-mode:vertical-rl;font-size:22px;font-weight:500;display:flex;align-items:center;justify-content:center}
.intro{left:61px;top:184px;width:670px;font-size:19px;font-weight:700;line-height:24px;color:var(--navy)}
.step{top:252px;width:320px;height:115px;border:1.5px dashed var(--blue);border-radius:8px}
.step-1{left:62px}.step-2{left:402px}
.step-num{position:absolute;font-size:86px;font-weight:700;color:var(--blue);line-height:1}
.step-1 .step-num{left:28px;top:6px}
.step-2 .step-num{left:44px;top:6px}
.step-text{position:absolute;font-size:19px;line-height:23px;color:var(--ink)}
.step-1 .step-text{left:71px;top:9px;width:240px}
.step-2 .step-text{left:101px;top:10px;width:210px}
.caution{left:62px;top:390px;width:659px;height:154px;background:var(--grey-panel);border-radius:10px;padding:19px 30px 0 38px;font-size:19px;line-height:23px}
.caution b{color:var(--red);font-weight:700}
.action-head,.drug-head{top:569px;height:46px;font-size:20px;font-weight:700;color:var(--white);text-align:center;line-height:46px;border-radius:8px 8px 0 0}
.action-head{left:63px;width:216px;background:var(--blue)}
.drug-head{left:282px;width:439px;background:var(--navy)}
.action-col{left:63px;top:613px;width:216px;height:484px;background:var(--navy);border-radius:8px 8px 8px 8px}
.drug-col{left:282px;top:613px;width:439px;height:484px;background:var(--grey-panel);border-radius:8px 8px 8px 8px}
.action-label{left:81px;font-size:19px;font-weight:700;line-height:23px;color:var(--white)}
.dot-rule{left:81px;width:180px;border-top:2px dotted #8a97a8}
.drug-rule{left:300px;width:400px;border-top:2px solid #d3d1d2}
.drug-text{left:308px;width:400px;font-size:19px;line-height:23px}
.drug-text p+p{margin-top:9px}
.range-title{left:776px;top:176px;width:575px;text-align:center}
.range-title .big{font-size:47px;font-weight:800;color:var(--teal);line-height:52px}
.range-title .small{font-size:31px;font-weight:500;letter-spacing:7.5px;color:var(--navy);line-height:40px}
.bp-col{top:289px;width:189px;height:252px;border-radius:12px;overflow:hidden;background:var(--blue)}
.bp-col div{height:68px;color:var(--white);font-size:19px;font-weight:700;text-align:center;line-height:68px}
.bp-col .bp-head{height:42px;line-height:44px;background:var(--navy);font-weight:600}
.bp-col .alt{background:var(--blue-deep);height:70px;line-height:70px}
.diff-box{left:784px;top:610px;width:547px;height:485px;border:1.5px dashed var(--blue);border-top:none;border-radius:0 16px 10px 10px}
.diff-box-cap{left:1298px;top:610px;width:33px;height:30px;border-top:1.5px dashed var(--blue);border-right:1.5px dashed var(--blue);border-radius:0 16px 0 0}
.diff-head{left:774px;top:570px;height:44px;padding:0 38px 0 30px;background:var(--navy);border-radius:22px 30px 0 22px;color:var(--white);font-size:21px;font-weight:700;line-height:46px}
.diff-line{left:1200px;top:609px;width:98px;height:5px;background:var(--navy)}
.diff-list{left:776px;top:640px;width:520px;list-style:none}
.diff-list li{position:absolute;left:0;width:520px;padding-left:27px;font-size:19px;line-height:23px}
.diff-list li::before{content:"";position:absolute;left:0;top:5px;width:15px;height:15px;border-radius:50%;background:var(--blue)}
</style>
</head>
<body>
<main class="card">
  <svg class="abs header-art" width="1505" height="160" viewBox="0 0 1505 160" aria-hidden="true">
    <defs>
      <linearGradient id="bandGrad" x1="0" x2="1" y1="0" y2="0">
        <stop offset="0" stop-color="#33a39b"/>
        <stop offset="0.5" stop-color="#3b86c6"/>
        <stop offset="1" stop-color="#3a74de"/>
      </linearGradient>
    </defs>
    <path d="M0 0H1505V136H760C742 150 725 157 690 157H0Z" fill="url(#bandGrad)"/>
    <path d="M748 136C772 52 790 22 850 22H1505V136Z" fill="#0b2540"/>
  </svg>
  <h1 class="abs title">HYPERTENSION, ACUTE</h1>
  <p class="abs subtitle">Sustained high blood pressure refractory<br>to treating reversible causes</p>
  <div class="abs page-tab">12</div>
  <div class="abs side-bar"></div>
  <div class="abs side-title">HYPERTENSION, ACUTE</div>
  <div class="abs revision">REVISION FEB 2020</div>

  <p class="abs intro">In pediatrics, hypertension is almost always treated by addressing likely causes such as light anesthesia or measurement error:</p>
  <div class="abs step step-1"><span class="step-num">1</span><p class="step-text">Ensure correct BP cuff size: cuff bladder width ~ 40% of limb circumference</p></div>
  <div class="abs step step-2"><span class="step-num">2</span><p class="step-text">Ensure arterial line transducer is at level of heart</p></div>

  <p class="abs caution"><b>CAUTION:</b> Anti-hypertensive drugs are almost never needed for routine pediatric cases. These medications are used almost&nbsp; exclusively for specialized cardiac, neurosurgical, or endocrine (pheochromocytoma) cases. Consult an expert before use. Rule-out increased ICP.</p>

  <div class="abs action-col"></div>
  <div class="abs drug-col"></div>
  <div class="abs action-head">ACTION</div>
  <div class="abs drug-head">DRUG (IV DOSING)</div>

  <p class="abs action-label" style="top:665px">Direct smooth<br>muscle relaxation</p>
  <div class="abs dot-rule" style="top:758px"></div>
  <p class="abs action-label" style="top:809px">β-Adrenergic<br>blockade</p>
  <div class="abs dot-rule" style="top:905px"></div>
  <p class="abs action-label" style="top:930px">Calcium channel<br>blockade</p>
  <div class="abs dot-rule" style="top:1006px"></div>
  <p class="abs action-label" style="top:1024px">D1-dopamine<br>agonist</p>

  <div class="abs drug-text" style="top:629px"><p>Sodium nitroprusside 0.5-10 MICROgrams/kg/min</p><p>HydrALAZINE 0.1-0.2 mg/kg (adult dose 5-10 mg)</p></div>
  <div class="abs drug-rule" style="top:758px"></div>
  <div class="abs drug-text" style="top:776px"><p>Esmolol 100-500 MICROgrams/kg over 5 min, then25-300 MICROgrams/kg/min</p><p>Labetalol (also a effect) 0.2-1 mg/kg q 10 min; 0.4-3 mg/kg/hour (infusion)</p></div>
  <div class="abs drug-rule" style="top:905px"></div>
  <div class="abs drug-text" style="top:931px"><p>niCARdapine 0.5-5 MICROgrams/kg/min</p><p>Clevidipine 0.5-3.5 MICROgrams/kg/min</p></div>
  <div class="abs drug-rule" style="top:1010px"></div>
  <div class="abs drug-text" style="top:1028px"><p>Fenoldopam 0.2-0.8 MICROgrams/kg/min</p></div>

  <div class="abs range-title"><div class="big">HYPERTENSIVE</div><div class="small">BLOOD PRESSURE RANGE*</div></div>
  <div class="abs bp-col" style="left:776px"><div class="bp-head">AGE (YR)</div><div>newborn</div><div class="alt">1-3</div><div>4-12</div></div>
  <div class="abs bp-col" style="left:969px"><div class="bp-head">SYSTOLIC</div><div>&gt;97</div><div class="alt">&gt;105</div><div>&gt;113</div></div>
  <div class="abs bp-col" style="left:1162px"><div class="bp-head">DIASTOLIC</div><div>&gt;70</div><div class="alt">&gt;61</div><div>&gt;86</div></div>

  <div class="abs diff-box"></div>
  <div class="abs diff-box-cap"></div>
  <div class="abs diff-line"></div>
  <h2 class="abs diff-head">CONSIDER DIFFERENTIAL (PARTIAL)</h2>
  <ul class="abs diff-list">
    <li style="top:2px">Light anesthesia (consider vaporizer or infusion pump empty or malfunctioning)</li>
    <li style="top:76px">Hypercarbia</li>
    <li style="top:127px">Hypoxemia</li>
    <li style="top:178px">Arterial line transducer too low or BP cuff too small</li>
    <li style="top:229px">Withdrawal (EtOH or opioid)</li>
    <li style="top:280px">Thyroid Storm</li>
    <li style="top:331px">Pheochromocytoma</li>
    <li style="top:383px">Drug Error</li>
  </ul>
</main>
</body>
</html>
```